Company Brochure / Sales Sheet

We would like a brochure that we will may print out as well as forward electronically to our prospective clients.

Our clients are inventors/doctors/surgeons of medical products who need help completing their medical product, gaining approval, and then selling their product into the US market

Target Market(s)

Inventors of medical products who want to sell them in the United States

Industry/Entity Type

Medical

Font styles to use
Serif
Sans Serif

Requirements
Must have
• The word "Medical" should not receive special empahsis.
• Use the last two photos and whatever other photos that look good. You can edit and crop the photos
• Text should be easy to read
Nice to have
• We want to show that we have a lot of products.
• Sharp, clean, modern
• Minimum two pages - final product should be capable of being printed and
• forwarded electronically
• Easy to read
Should not have
• Should not be cluttered

```html
<!DOCTYPE html>
<html lang="en">
<head>
<meta charset="utf-8">
<title>Meridian Care Network – Brochure</title>
<link href="https://fonts.googleapis.com/css2?family=Lato:wght@400;700&family=Exo+2:ital,wght@1,700&display=swap" rel="stylesheet">
<style>
  :root{
    --navy:#1b2a6b;
    --navy-deep:#14205a;
    --red:#d7261e;
    --maroon:#6e1a1f;
    --ink:#1a1a1a;
    --paper:#ffffff;
    --paper-grey:#eef0f4;
    --photo-blue:#5f9ad0;
    --photo-light:#c9dff0;
    --steel:#b9bfc7;
  }
  *{margin:0;padding:0;box-sizing:border-box}
  html,body{width:1200px;height:778px;overflow:hidden;background:var(--paper)}
  .canvas{position:relative;width:1200px;height:778px;background:var(--paper);font-family:'Lato',sans-serif;color:var(--ink)}

  /* Cover page */
  .cover{position:absolute;left:14px;top:12px;width:582px;height:750px;overflow:hidden;background:linear-gradient(180deg,#fff 0%,var(--paper-grey) 100%);border-bottom:3px solid var(--navy-deep)}
  .cover svg{position:absolute;left:0;top:0}
  .brand{position:absolute;left:395px;top:30px;width:180px;text-align:center;color:#fff}
  .brand-mark{width:30px;height:30px;border-radius:50%;background:#fff;margin:0 auto 6px}
  .brand-name{font-size:10px;font-weight:700;letter-spacing:.4px}
  .brand-sub{font-size:7px;letter-spacing:5px;margin-top:2px}
  .tagline{position:absolute;left:360px;top:100px;width:240px;text-align:center;color:#fff;font-family:'Exo 2',sans-serif;font-style:italic;font-weight:700;font-size:16.5px;line-height:21px}

  /* Inside page */
  .inside{position:absolute;left:604px;top:12px;width:582px;height:750px;background:linear-gradient(135deg,#fff 0%,var(--paper-grey) 100%);border-top:7px solid var(--navy-deep);border-bottom:3px solid var(--navy-deep)}
  .col{position:absolute;top:22px;width:259px}
  .col-left{left:23px}
  .col-right{left:300px}
  .col h2{font-size:16.5px;font-weight:700;color:var(--ink);margin-bottom:6px;letter-spacing:-.2px}
  .col p{font-size:11.2px;line-height:13.75px;text-align:justify;text-indent:34px}
  .col section + section{margin-top:15px}

  .gallery{position:absolute;left:22px;top:475px;display:grid;grid-template-columns:repeat(4,119px);grid-template-rows:repeat(2,119px);column-gap:21px;row-gap:10px}
  .tile{border:2px solid var(--navy);background:linear-gradient(160deg,#fafafa,#d8dce2)}
  .tile.blue{background:linear-gradient(160deg,#9fc7ee,#2d5fb0)}
  .tile.drape{background:linear-gradient(160deg,#e4e8ee,#1e3780)}
</style>
</head>
<body>
<div class="canvas">

  <div class="cover">
    <svg width="582" height="750" viewBox="0 0 582 750">
      <rect x="0" y="60" width="582" height="520" fill="url(#photoTone)" role="img" aria-label="Photo of a hand touching a digital medical interface beside a glowing globe"/>
      <defs>
        <linearGradient id="photoTone" x1="0" y1="0" x2="1" y2="1">
          <stop offset="0" stop-color="#2f5f9a"/>
          <stop offset=".5" stop-color="#7fb2de"/>
          <stop offset="1" stop-color="#c9dff0"/>
        </linearGradient>
      </defs>
      <path d="M0,0 H582 V175 C470,195 330,150 200,80 C130,40 60,15 0,20 Z" fill="#1b2a6b"/>
      <path d="M20,0 C120,20 260,120 380,160 C460,186 530,190 582,172" fill="none" stroke="#fff" stroke-width="9"/>
      <path d="M0,380 C140,360 260,440 380,520 C460,570 530,560 582,500 V750 H0 Z" fill="#6e1a1f"/>
      <path d="M0,390 C150,375 270,470 390,545 C470,590 540,575 582,520 V750 H0 Z" fill="#d7261e"/>
      <path d="M0,470 C160,470 280,560 400,600 C480,625 550,600 582,570 V750 H0 Z" fill="#1b2a6b"/>
      <path d="M0,520 C170,525 300,600 420,625 C500,640 560,620 582,605 V750 H0 Z" fill="#f2f3f6"/>
      <g fill="#b9bfc7" role="img" aria-label="Photos of surgical instruments: rongeurs, forceps, cutters, elevators and a mallet">
        <rect x="200" y="572" width="140" height="14" rx="4"/>
        <rect x="75" y="610" width="150" height="55" rx="6"/>
        <rect x="260" y="610" width="145" height="55" rx="6"/>
        <rect x="425" y="600" width="145" height="60" rx="6"/>
        <rect x="32" y="685" width="170" height="50" rx="6"/>
        <rect x="230" y="682" width="145" height="14" rx="4"/>
        <rect x="245" y="724" width="135" height="10" rx="3"/>
        <rect x="420" y="685" width="140" height="42" rx="6"/>
      </g>
    </svg>
    <div class="brand">
      <div class="brand-mark"></div>
      <div class="brand-name">MERIDIAN CARE</div>
      <div class="brand-sub">NETWORK</div>
    </div>
    <div class="tagline">Saving Lives And Reducing<br>Health Care Costs</div>
  </div>

  <div class="inside">
    <div class="col col-left">
      <section>
        <h2>About Us</h2>
        <p>We are a network of medical distribution professionals including physicians and surgeons, regulatory and coding experts, patent and trademark lawyers, international fulfillment experts, marketing and advertising professionals, and business strategists all working together in the distribution of promising new medical products. We handle all aspects of new surgical product sales, marketing, and distribution.</p>
        <p>Our company was founded in Milford, Delaware, with distribution locations and support associates and affiliates located throughout the US. We have extensive experience with medical product development, intellectual property, and regulatory and compliances issues.</p>
        <p>We partner with medical innovators by providing strategic support with intellectual property and regulatory approval, reimbursement coding, marketing, selling and distributing state of the art medical products. Our clients include highly creative medical companies with strong management teams and consumer-driven growth perspectives.</p>
        <p>Our products are uniquely positioned in an evolving health sector to offer benefits to patients, healthcare institutions, medical professionals, insurance companies and governmental agencies. Our evidence-based technologies reduce overall healthcare expenses and empower physicians and surgeons to provide improved practices and standards of care.</p>
      </section>
    </div>

    <div class="col col-right">
      <section>
        <h2>Medical Products</h2>
        <p>We specialize in the distribution of next generation medical products including customized surgical instruments and kits, monitoring and diagnostic devices, advanced wound care products and innovative acute care disposables</p>
        <p>Our medical products represent breakthroughs in medical technology, saving lives, reducing health care costs, improving patient lifestyles.</p>
      </section>
      <section>
        <h2>Intellectual Property and Branding</h2>
        <p>We help our partners get the trademarks and patent claim approvals they need and deserve and at a reasonable price. Our team of patent attorneys and agents is effective and affordable and has gained over 300 client patent approvals. We help our clients brand and position their products for successful product launches and introductions to the US market.</p>
      </section>
      <section>
        <h2>Regulatory Issues</h2>
        <p>We provide comprehensive services support for global physician inventors who are seeking to distribute their medical products within the United States. We assist in navigating the unique aspects of the US medical market -- including FDA compliance and device returns, US Customs, and reimbursement coding.</p>
      </section>
    </div>

    <div class="gallery">
      <div class="tile" role="img" aria-label="Photo of bone cutting pliers"></div>
      <div class="tile" role="img" aria-label="Photo of needle holder tips"></div>
      <div class="tile blue" role="img" aria-label="Photo of blue coated forceps"></div>
      <div class="tile blue" role="img" aria-label="Photo of a yellow disposable instrument on blue"></div>
      <div class="tile" role="img" aria-label="Photo of a long laparoscopic grasper"></div>
      <div class="tile" role="img" aria-label="Photo of curved clamp jaws"></div>
      <div class="tile" role="img" aria-label="Photo of angled scissors"></div>
      <div class="tile drape" role="img" aria-label="Photo of a sterile wound care pad on blue drape"></div>
    </div>
  </div>

</div>
</body>
</html>
```